Flyer Design Project

We are a restaurant meal delivery service. We deliver from a variety of restaurants. We would like a flyer that will promote our service to busy commuters. The flyer will be distributed at local train stations. I would like the flyer to say something like "What's for dinner?" or "Meet us at your place!" or anything that is catchy.
In the flyer we want the customer to order online at our website plateswiftly.com and use coupon code $5off. Using the coupon code will get them $5 off of their online purchase.
We would like to pass the flyers out in the morning and have the customers go online either on the train or at work to schedule the food to be delivered for dinner.
Target Market(s)
Hungry commuters that are in a rush 30 - 50 women
Industry/Entity Type
Restaurant

```html
<!DOCTYPE html>
<html lang="en">
<head>
<meta charset="utf-8">
<title>Plate Swiftly – Meet us at your place!</title>
<link rel="stylesheet" href="https://fonts.googleapis.com/css2?family=Crimson+Text:ital,wght@0,400;0,600;0,700;1,700&display=swap">
<style>
  :root {
    --paper: #f4f1ea;
    --paper-edge: #e6e2d8;
    --ink: #1e1b18;
    --maroon: #9b1c26;
    --orange: #e8731f;
    --white: #ffffff;
    --card: #d9d6cf;
  }
  * { margin: 0; padding: 0; box-sizing: border-box; }
  html, body { width: 958px; height: 1200px; overflow: hidden; }
  body {
    font-family: "Crimson Text", Georgia, serif;
    color: var(--ink);
    background: var(--paper);
  }
  .flyer {
    position: relative;
    width: 958px;
    height: 1200px;
    overflow: hidden;
    background: radial-gradient(ellipse at 70% 40%, #fbf9f4 0%, var(--paper) 55%, var(--paper-edge) 100%);
  }
  .food-photo {
    position: absolute;
    left: -160px;
    top: -215px;
    width: 790px;
    height: 790px;
    border-radius: 50%;
    background:
      radial-gradient(circle at 62% 52%, #f5f2ea 0 6%, transparent 7%),
      radial-gradient(ellipse at 55% 75%, #c2401c 0%, #a8301a 35%, #7e2413 65%, transparent 80%),
      linear-gradient(180deg, #3d5a2a 0%, #5c7a3a 30%, #b8b4a8 45%, #b33a1c 60%, #8a2a15 100%);
    box-shadow: 0 6px 14px rgba(0,0,0,0.25);
  }
  .coupon { position: absolute; left: 30px; top: 464px; width: 420px; height: 310px; }
  .coupon svg { position: absolute; inset: 0; }
  .coupon-amount {
    position: absolute; left: 70px; top: 64px; width: 140px;
    text-align: center; color: var(--white);
    font-size: 36px; font-weight: 600; line-height: 46px;
  }
  .coupon-text {
    position: absolute; left: 200px; top: 58px; width: 200px;
    text-align: center; color: var(--white);
    font-size: 23px; font-weight: 600; line-height: 29px;
  }
  .tagline {
    position: absolute; right: 30px; top: 22px;
    font-size: 29px; font-weight: 700;
  }
  .brand {
    position: absolute; right: 30px; top: 268px;
    display: flex; align-items: center; gap: 14px;
    white-space: nowrap;
  }
  .brand-dot { flex: none; width: 24px; height: 24px; border-radius: 50%; background: var(--maroon); }
  .brand-name { color: var(--maroon); font-size: 48px; font-weight: 700; line-height: 1; }
  .instructions { position: absolute; right: 30px; top: 396px; text-align: right; }
  .instructions h2 { font-size: 36px; font-weight: 600; line-height: 40px; margin-bottom: 14px; }
  .steps { list-style: none; }
  .steps li { font-size: 24px; font-weight: 600; line-height: 33px; margin-bottom: 27px; }
  .step-num { font-size: 40px; font-style: italic; font-weight: 700; }
  .detail { position: absolute; left: 98px; top: 798px; }
  .detail h3 { font-size: 22px; font-weight: 700; margin-bottom: 8px; }
  .detail ul { list-style: none; font-size: 17px; }
  .detail li { position: relative; padding-left: 22px; margin-bottom: 11px; line-height: 20px; }
  .detail li::before { content: "•"; position: absolute; left: 2px; }
  .divider { position: absolute; left: 476px; top: 794px; width: 6px; height: 228px; background: var(--orange); border-radius: 3px; }
  .addons { position: absolute; left: 553px; top: 772px; width: 272px; }
  .addons h3 { text-align: center; font-size: 21px; font-weight: 700; margin-bottom: 4px; }
  .addon-list { list-style: none; font-size: 15.5px; }
  .addon-list li { display: flex; height: 22px; align-items: baseline; white-space: nowrap; }
  .addon-list .dots { flex: 1; border-bottom: 1.5px dotted var(--ink); margin: 0 2px; min-width: 12px; }
  .addon-list .size { width: 52px; }
  .addon-note { font-size: 11.5px; margin-top: 2px; white-space: nowrap; }
  .cards {
    position: absolute; left: 35px; top: 1048px; width: 126px; height: 86px;
    background: var(--white); padding: 8px;
    display: grid; grid-template-columns: 1fr 1fr; gap: 6px;
  }
  .card-badge { background: var(--card); border: 1px solid #b9b5ad; }
  .hours { position: absolute; left: 0; right: 0; top: 1078px; text-align: center; }
  .hours h4 { color: var(--maroon); font-size: 20px; font-weight: 600; }
  .hours h4 span { font-size: 17px; }
  .hours p { font-size: 16px; margin-top: 4px; padding-left: 40px; }
  .hours b { font-size: 17px; }
  .hours .sep { margin: 0 14px; }
  .order-online {
    position: absolute; left: 35px; right: 31px; top: 1134px;
    display: flex; justify-content: space-between; align-items: baseline;
    white-space: nowrap;
  }
  .order-online span { font-size: 29px; font-weight: 600; }
  .order-online strong { font-size: 46px; font-weight: 600; }
</style>
</head>
<body>
<main class="flyer">
  <div class="food-photo" role="img" aria-label="Photo of glazed chicken wings with celery, carrot sticks and a dip"></div>

  <div class="coupon">
    <svg viewBox="0 0 420 310" width="420" height="310" aria-hidden="true">
      <defs>
        <radialGradient id="couponFill" cx="50%" cy="45%" r="60%">
          <stop offset="0" stop-color="#d8532a"/>
          <stop offset="1" stop-color="#9b1c26"/>
        </radialGradient>
        <linearGradient id="amountFill" x1="0" y1="0" x2="0" y2="1">
          <stop offset="0" stop-color="#f39a3c"/>
          <stop offset="1" stop-color="#e26a1a"/>
        </linearGradient>
      </defs>
      <path d="M8 140 C8 50 110 4 215 4 C340 4 405 70 405 150 C405 205 392 255 412 306 C360 272 320 282 215 282 C95 282 8 232 8 140 Z" fill="url(#couponFill)"/>
      <path d="M20 140 C20 58 115 16 215 16 C330 16 392 78 392 150 C392 200 382 238 392 282 C352 260 312 268 215 268 C105 268 20 225 20 140 Z" fill="none" stroke="var(--white)" stroke-width="2" stroke-dasharray="9 6"/>
      <ellipse cx="250" cy="146" rx="134" ry="94" fill="none" stroke="var(--white)" stroke-width="2"/>
      <circle cx="140" cy="88" r="68" fill="url(#amountFill)"/>
    </svg>
    <div class="coupon-amount">$5 off</div>
    <p class="coupon-text">Using<br>the coupon<br>code will getof<br>their online<br>purchase</p>
  </div>

  <p class="tagline">Meet us at your place!</p>

  <div class="brand">
    <span class="brand-dot"></span>
    <span class="brand-name">Plate Swiftly</span>
  </div>

  <section class="instructions">
    <h2>Online Ordering<br>Instructions</h2>
    <ol class="steps">
      <li><span class="step-num">1</span>. Select a Restaurant</li>
      <li><span class="step-num">2</span>. Choose Delivery<br>Time &amp; Items</li>
      <li><span class="step-num">3</span>. RELAX Your<br>Meal will arrive as scheduled</li>
    </ol>
  </section>

  <section class="detail">
    <h3>Detail</h3>
    <ul>
      <li>$15 Minimum Order</li>
      <li>Delivery $3.99</li>
      <li>Prices and menu items are<br>subject to change without notice</li>
      <li>All Credit Cards are accepted</li>
      <li>Company Checks OK</li>
    </ul>
  </section>

  <div class="divider" role="img" aria-label="Decorative orange divider"></div>

  <section class="addons">
    <h3>Add-Ons</h3>
    <ul class="addon-list">
      <li>• Cola<span class="dots"></span><span class="size">12oz.</span><span class="dots"></span>$0.75</li>
      <li>• Cola<span class="dots"></span><span class="size">6-pack</span><span class="dots"></span>$4.25</li>
      <li>• Diet Cola<span class="dots"></span><span class="size">12oz.</span><span class="dots"></span>$0.75</li>
      <li>• Diet Cola<span class="dots"></span><span class="size">6-pack</span><span class="dots"></span>$4.25</li>
      <li>• Lemon Soda<span class="dots"></span><span class="size">12oz.</span><span class="dots"></span>$0.75</li>
      <li>• Lemon Soda<span class="dots"></span><span class="size">6-pack</span><span class="dots"></span>$4.25</li>
      <li>• Plates<span class="dots"></span>$.20 per</li>
      <li>• Cups<span class="dots"></span>$.15 per</li>
      <li>• Plastic ware<span class="dots"></span>$.25 per</li>
    </ul>
    <p class="addon-note">Includes knife, fork, spoon, napkin and salt &amp; pepper</p>
  </section>

  <div class="cards" aria-label="Accepted payment cards">
    <span class="card-badge"></span><span class="card-badge"></span>
    <span class="card-badge"></span><span class="card-badge"></span>
  </div>

  <section class="hours">
    <h4>Hours : <span>Call Center Hours</span></h4>
    <p><b>Mon-Fri Lunch</b>&nbsp;&nbsp; 11:00-2pm <span class="sep">|</span> <b>Dinner</b>&nbsp;&nbsp; 4:00-9pm <span class="sep">|</span> <b>Sat-Sun</b>&nbsp;&nbsp;&nbsp;&nbsp; 5pm-9pm</p>
  </section>

  <p class="order-online"><span>order online at our website</span><strong>www.plateswiftly.com</strong></p>
</main>
</body>
</html>
```